Valdorick Business Card Design

Valdorick is the holdings company for my portfolio of businesses. These businesses currently only include Valdorick Advising. V|A is a strategic consulting firm that focuses on small businesses and start-ups that want help with their brand. We focus on partnering with influencers (Pro Athletes and Celebrities) and Social Media Marketing. We also want to focus on companies that have a positive effect on the community or world. The audience I am going after is very corporate. I want to have the corporate edge with some 25yr old flair.
Industry/Entity Type
Business
Contact Information for Business Card
General Idea AttachedLogo (Attached)Jonathan R. MasonCEO & Managing MemberDown Left Bottom CornerPhone: 347-570-0585Cell: 240-604-7930mason@valdorick-example.comDown Right Bottom Corner 174 W 4th St, Ste 212New York, NY 10014www.valdorick-example.comBackside LogoI want the entire card extra thick and with metallic finish
Look and feel

```html
<!DOCTYPE html>
<html lang="en">
<head>
<meta charset="utf-8">
<title>Valdorick Holdings – Business Card</title>
<link href="https://fonts.googleapis.com/css2?family=Open+Sans:wght@400;600&display=swap" rel="stylesheet">
<style>
  :root {
    --backdrop: #c9cbce;
    --card: #fbfbfb;
    --ink: #5a5c60;
    --ink-soft: #77797d;
    --accent: #b01e2c;
    --rule: #6d6f73;
  }
  * { box-sizing: border-box; margin: 0; padding: 0; }
  html, body {
    width: 1200px; height: 713px; overflow: hidden;
    background: var(--backdrop);
    font-family: "Open Sans", Arial, sans-serif;
  }
  .stage {
    width: 1200px; height: 713px;
    display: flex; align-items: center; justify-content: center;
  }
  .business-card {
    position: relative;
    width: 840px; height: 480px;
    background: var(--card);
    box-shadow: 0 6px 18px rgba(0,0,0,.12);
    color: var(--ink);
  }
  .brand {
    position: absolute; left: 120px; top: 92px;
    display: flex; align-items: flex-end; gap: 18px;
  }
  .brand-square {
    width: 74px; height: 74px; background: var(--accent);
  }
  .brand-name {
    font-size: 30px; font-weight: 600; letter-spacing: 1px;
    color: var(--accent); text-transform: uppercase;
    padding-bottom: 8px;
    border-bottom: 1.5px solid var(--ink-soft);
    line-height: 1.1;
  }
  .person {
    position: absolute; left: 230px; top: 196px;
  }
  .person-name {
    font-size: 36px; font-weight: 400; color: var(--ink);
    line-height: 1.1;
  }
  .person-title {
    margin-top: 4px; padding-top: 4px;
    border-top: 1.5px solid var(--accent);
    font-size: 15px; color: var(--accent); padding-left: 30px;
  }
  .address {
    position: absolute; right: 44px; top: 178px;
    text-align: right; font-size: 19px; line-height: 1.35;
    color: var(--ink-soft);
  }
  .contacts {
    position: absolute; left: 44px; top: 330px;
    list-style: none; font-size: 20px; line-height: 1.3;
    color: var(--ink-soft);
  }
  .contacts li { display: flex; align-items: center; gap: 10px; }
  .contacts svg { width: 18px; height: 18px; fill: none; stroke: var(--ink); stroke-width: 1.8; }
  .card-rule {
    position: absolute; left: 44px; right: 44px; top: 432px;
    height: 2px; background: var(--rule);
  }
</style>
</head>
<body>
<main class="stage">
  <section class="business-card">
    <div class="brand">
      <span class="brand-square"></span>
      <span class="brand-name">Valdorick Holdings LLC</span>
    </div>

    <div class="person">
      <h1 class="person-name">Derrick L. Fanshaw</h1>
      <p class="person-title">CEO &amp; Managing Member</p>
    </div>

    <address class="address">
      88 E 9th St, Ste 405<br>
      New York, NY 10099<br>
      www.valdorick-example.com
    </address>

    <ul class="contacts">
      <li>
        <svg viewBox="0 0 20 20" aria-hidden="true"><path d="M3 8c0-3 3-4 7-4s7 1 7 4l-3 1-1-2H7L6 9z M5 11h10v5H5z"/></svg>
        347-555-0162
      </li>
      <li>
        <svg viewBox="0 0 20 20" aria-hidden="true"><rect x="6" y="2" width="8" height="16" rx="1.5"/></svg>
        240-555-0187
      </li>
      <li>
        <svg viewBox="0 0 20 20" aria-hidden="true"><rect x="3" y="5" width="14" height="10"/><path d="M3 5l7 6 7-6"/></svg>
        fanshaw@valdorick-example.com
      </li>
    </ul>

    <div class="card-rule"></div>
  </section>
</main>
</body>
</html>
```